Brightfen Holdings Brochure for potential buyers

Nice, modern looking brochure with our logo and information about a property we are selling. Should display all the property features as well as information about the location. Same color scheme as the flyer i've attached (black, green, gold). Please see website for verbiage to use: www.brightfenholdings-sample.com/ravensby

Target Market(s)

Potential Buyers, Real Estate agents

Industry/Entity Type

Real Estate

Font styles to use
Sans Serif

Colors
9bcb3c
fbf289
000000
fbfbfb

Requirements
Must have
• Photos, Logo, Phone number, Green-Black-Gold color scheme. Property information and Location information can be obtained from www.brightfenholdings-sample.com/ravensby

```html
<!DOCTYPE html>
<html lang="en">
<head>
<meta charset="utf-8">
<title>Brightfen Holdings – Property Brochure</title>
<link rel="stylesheet" href="https://fonts.googleapis.com/css2?family=Open+Sans:wght@400;600;700&display=swap">
<style>
  :root {
    --board: #e9e9e9;
    --paper: #ffffff;
    --green: #659b7d;
    --green-text: #5c9472;
    --gold: #dcc22f;
    --ink: #1a1a1a;
    --muted: #555555;
    --on-green: #eef4f0;
    --divider: #c9c9c9;
  }
  * { box-sizing: border-box; margin: 0; padding: 0; }
  html, body { width: 1200px; height: 900px; overflow: hidden; }
  body {
    background: var(--board);
    font-family: "Open Sans", Arial, sans-serif;
    position: relative;
  }
  .brochure {
    position: absolute;
    top: 42px;
    width: 540px;
    height: 766px;
    background: var(--paper);
    box-shadow: 3px 4px 5px rgba(0,0,0,.35);
  }
  .brochure--green { left: 50px; }
  .brochure--light { left: 610px; }

  /* sidebar */
  .sidebar {
    position: absolute; left: 0; top: 0; width: 200px; height: 100%;
  }
  .brand {
    position: absolute; top: 78px; left: 0; width: 200px;
    text-align: center;
    color: var(--green-text);
    font-weight: 700;
    font-size: 27px;
    line-height: 32px;
    letter-spacing: .5px;
  }
  .fact { position: absolute; left: 0; width: 200px; text-align: center; }
  .fact svg { display: block; margin: 0 auto 4px; }
  .fact__label { color: var(--muted); font-size: 14px; line-height: 20px; }
  .fact__value { color: var(--green-text); font-size: 14px; font-weight: 700; line-height: 21px; }
  .fact--location { top: 146px; }
  .fact--type { top: 229px; }
  .fact--area { top: 312px; }
  .fact--price { top: 395px; }

  .features-title {
    position: absolute; top: 509px; left: 0;
    width: 187px; height: 28px;
    background: var(--green);
    border-radius: 0 14px 14px 0;
    color: #fff; font-weight: 700; font-size: 17px;
    line-height: 28px; padding-left: 16px;
  }
  .features {
    position: absolute; top: 548px; left: 18px; width: 180px;
    list-style: none;
    color: var(--green-text); font-weight: 700; font-size: 11.5px; line-height: 15.3px;
  }
  .features li { position: relative; padding-left: 15px; }
  .features li::before {
    content: ""; position: absolute; left: 0; top: 6px;
    width: 4px; height: 4px; border-radius: 50%; background: var(--green-text);
  }

  /* description panel */
  .panel {
    position: absolute; left: 200px; top: 0; width: 340px; height: 100%;
  }
  .brochure--green .panel { background: var(--green); color: var(--on-green); }
  .brochure--light .panel { background: var(--paper); color: var(--ink); border-left: 3px solid var(--divider); }
  .panel__title {
    position: absolute; top: 44px; right: 30px;
    font-size: 23px; font-weight: 700; line-height: 28px;
  }
  .brochure--green .panel__title { color: #fff; }
  .brochure--light .panel__title { color: var(--ink); }
  .panel__photo {
    position: absolute; top: 83px; left: 0; width: 308px; height: 181px;
    border-radius: 0 10px 10px 0;
    background: linear-gradient(180deg, #7fb0dc 0%, #b9d3ea 45%, #6e6f72 58%, #c9a98a 68%, #d9c2a0 100%);
  }
  .brochure--light .panel__photo { left: -3px; width: 309px; }
  .panel__copy {
    position: absolute; left: 22px; width: 290px;
    font-size: 7.6px; line-height: 10.6px; text-align: justify;
  }
  .panel__copy p + p { margin-top: 10.6px; }
  .panel__copy--intro { top: 285px; }
  .panel__copy--closing { top: 670px; }

  .highlights {
    position: absolute; top: 545px; left: 0; width: 100%; height: 120px;
    background: var(--gold);
    color: var(--ink);
  }
  .brochure--light .highlights { left: -3px; width: 343px; }
  .highlights ul {
    list-style: none; position: absolute; top: 4px; left: 22px; width: 290px;
    font-size: 7.8px; line-height: 11px;
  }
  .highlights li { position: relative; padding-left: 10px; }
  .highlights li::before {
    content: ""; position: absolute; left: 1px; top: 4.5px;
    width: 3px; height: 3px; border-radius: 50%; background: var(--ink);
  }

  .note {
    position: absolute; top: 834px; left: 0; width: 1200px;
    text-align: center; font-size: 16.5px; color: #111;
  }
</style>
</head>
<body>

<article class="brochure brochure--green">
  <aside class="sidebar">
    <div class="brand">Brightfen<br>Holdings</div>

    <div class="fact fact--location">
      <svg width="16" height="22" viewBox="0 0 16 22"><path d="M8 0C3.6 0 0 3.4 0 7.8 0 13.5 8 22 8 22s8-8.5 8-14.2C16 3.4 12.4 0 8 0z" fill="#5c9472"/><circle cx="8" cy="8" r="3.2" fill="#fff"/></svg>
      <div class="fact__label">Location</div>
      <div class="fact__value">City of Ravensby</div>
    </div>
    <div class="fact fact--type">
      <svg width="24" height="24" viewBox="0 0 24 24"><circle cx="12" cy="12" r="12" fill="#5c9472"/><rect x="6.5" y="6.5" width="4.5" height="4.5" fill="#fff"/><rect x="13" y="6.5" width="4.5" height="4.5" fill="#fff"/><rect x="6.5" y="13" width="4.5" height="4.5" fill="#fff"/><rect x="13" y="13" width="4.5" height="4.5" fill="#fff"/></svg>
      <div class="fact__label">Type</div>
      <div class="fact__value">Condo Industrial</div>
    </div>
    <div class="fact fact--area">
      <svg width="24" height="24" viewBox="0 0 24 24"><circle cx="12" cy="12" r="12" fill="#5c9472"/><path d="M6 7h12v7l-4 4H6z" fill="#fff"/><path d="M14 18v-4h4" fill="#5c9472"/></svg>
      <div class="fact__label">Area (SF)</div>
      <div class="fact__value">29,925</div>
    </div>
    <div class="fact fact--price">
      <svg width="24" height="24" viewBox="0 0 24 24"><circle cx="12" cy="12" r="12" fill="#5c9472"/><text x="12" y="17" text-anchor="middle" font-family="Open Sans, sans-serif" font-weight="700" font-size="14" fill="#fff">$</text></svg>
      <div class="fact__label">Price</div>
      <div class="fact__value">$6,749,900</div>
    </div>

    <div class="features-title">Other Features:</div>
    <ul class="features">
      <li>Roof capable of holding 53 HVAC units (7.5 ton)</li>
      <li>POWER Ready NOW!</li>
      <li>New Roads</li>
      <li>24 hour guarded community</li>
      <li>Dedicated cultivation water, gas, and electrical systems</li>
      <li>22,000 sqft canopies (max allowed by state law)</li>
    </ul>
  </aside>

  <section class="panel">
    <h2 class="panel__title">Property Description</h2>
    <div class="panel__photo" role="img" aria-label="Photo of the industrial building behind a site fence with a sales sign, desert ground and blue sky"></div>
    <div class="panel__copy panel__copy--intro">
      <p>Introducing Kestrel Industrial Park, a Northgate Build Group Development. Our team of world-class development and cannabis experts is designing cutting-edge business parks that meet the precise state and local legal requirements for allowable cultivation, manufacturing, extraction and testing.</p>
      <p>From 24-hour security patrols and gated entry to state-of-the-art cultivation water and electrical systems, our efficient designs help cut costs and reduce worry – something that other sites don’t offer.</p>
      <p>4th Quarter 2017 Move In!</p>
      <p>Have your business up and running by the start of 2018!</p>
      <p>The City of Ravensby is the epicenter of medical marijuana cultivation and manufacturing in the Western United States, and Kestrel Industrial Park is situated in the heart of Ravensby’s designated Medical Marijuana Cultivation and Manufacturing Zone.</p>
      <p>This 29,925 square foot concrete tilt up building has power capability like NO ONE ELSE. Dont be fooled by other buildings who “claim” to have enough power. Do your research!! 7 buildings currently being marketed and ready (of the 21 total future buildings in the complex.) The entire property has an approved Conditional Use Permit for Cultivation.</p>
    </div>
    <div class="highlights">
      <ul>
        <li>Development agreement with the City of Ravensby to include a future guarantee of a use permit for the next 10 years.</li>
        <li>2500 amp/ 3 phase / 480 V per unit</li>
        <li>Standard Office with (1) 2 ton HVAC</li>
        <li>ESFR Fire Sprinkler System Throughout</li>
        <li>New Lighting and New Plumbing</li>
        <li>ADA Restrooms</li>
        <li>Buyer will be responsible for its own tenant improvements</li>
        <li>City approved tenant improvement plans can be provided upon buyers’ request to demonstrate potential layout options</li>
      </ul>
    </div>
    <div class="panel__copy panel__copy--closing">
      <p>The City of Ravensby is geographically located between Las Vegas and Los Angeles where its warm weather, robust labor force, and convenient freeway access offers an ideal setting for indoor cultivation and distribution of medical marijuana.</p>
    </div>
  </section>
</article>

<article class="brochure brochure--light">
  <aside class="sidebar">
    <div class="brand">Brightfen<br>Holdings</div>

    <div class="fact fact--location">
      <svg width="16" height="22" viewBox="0 0 16 22"><path d="M8 0C3.6 0 0 3.4 0 7.8 0 13.5 8 22 8 22s8-8.5 8-14.2C16 3.4 12.4 0 8 0z" fill="#5c9472"/><circle cx="8" cy="8" r="3.2" fill="#fff"/></svg>
      <div class="fact__label">Location</div>
      <div class="fact__value">City of Ravensby</div>
    </div>
    <div class="fact fact--type">
      <svg width="24" height="24" viewBox="0 0 24 24"><circle cx="12" cy="12" r="12" fill="#5c9472"/><rect x="6.5" y="6.5" width="4.5" height="4.5" fill="#fff"/><rect x="13" y="6.5" width="4.5" height="4.5" fill="#fff"/><rect x="6.5" y="13" width="4.5" height="4.5" fill="#fff"/><rect x="13" y="13" width="4.5" height="4.5" fill="#fff"/></svg>
      <div class="fact__label">Type</div>
      <div class="fact__value">Condo Industrial</div>
    </div>
    <div class="fact fact--area">
      <svg width="24" height="24" viewBox="0 0 24 24"><circle cx="12" cy="12" r="12" fill="#5c9472"/><path d="M6 7h12v7l-4 4H6z" fill="#fff"/><path d="M14 18v-4h4" fill="#5c9472"/></svg>
      <div class="fact__label">Area (SF)</div>
      <div class="fact__value">29,925</div>
    </div>
    <div class="fact fact--price">
      <svg width="24" height="24" viewBox="0 0 24 24"><circle cx="12" cy="12" r="12" fill="#5c9472"/><text x="12" y="17" text-anchor="middle" font-family="Open Sans, sans-serif" font-weight="700" font-size="14" fill="#fff">$</text></svg>
      <div class="fact__label">Price</div>
      <div class="fact__value">$6,749,900</div>
    </div>

    <div class="features-title">Other Features:</div>
    <ul class="features">
      <li>Roof capable of holding 53 HVAC units (7.5 ton)</li>
      <li>POWER Ready NOW!</li>
      <li>New Roads</li>
      <li>24 hour guarded community</li>
      <li>Dedicated cultivation water, gas, and electrical systems</li>
      <li>22,000 sqft canopies (max allowed by state law)</li>
    </ul>
  </aside>

  <section class="panel">
    <h2 class="panel__title">Property Description</h2>
    <div class="panel__photo" role="img" aria-label="Photo of the industrial building behind a site fence with a sales sign, desert ground and blue sky"></div>
    <div class="panel__copy panel__copy--intro">
      <p>Introducing Kestrel Industrial Park, a Northgate Build Group Development. Our team of world-class development and cannabis experts is designing cutting-edge business parks that meet the precise state and local legal requirements for allowable cultivation, manufacturing, extraction and testing.</p>
      <p>From 24-hour security patrols and gated entry to state-of-the-art cultivation water and electrical systems, our efficient designs help cut costs and reduce worry – something that other sites don’t offer.</p>
      <p>4th Quarter 2017 Move In!</p>
      <p>Have your business up and running by the start of 2018!</p>
      <p>The City of Ravensby is the epicenter of medical marijuana cultivation and manufacturing in the Western United States, and Kestrel Industrial Park is situated in the heart of Ravensby’s designated Medical Marijuana Cultivation and Manufacturing Zone.</p>
      <p>This 29,925 square foot concrete tilt up building has power capability like NO ONE ELSE. Dont be fooled by other buildings who “claim” to have enough power. Do your research!! 7 buildings currently being marketed and ready (of the 21 total future buildings in the complex.) The entire property has an approved Conditional Use Permit for Cultivation.</p>
    </div>
    <div class="highlights">
      <ul>
        <li>Development agreement with the City of Ravensby to include a future guarantee of a use permit for the next 10 years.</li>
        <li>2500 amp/ 3 phase / 480 V per unit</li>
        <li>Standard Office with (1) 2 ton HVAC</li>
        <li>ESFR Fire Sprinkler System Throughout</li>
        <li>New Lighting and New Plumbing</li>
        <li>ADA Restrooms</li>
        <li>Buyer will be responsible for its own tenant improvements</li>
        <li>City approved tenant improvement plans can be provided upon buyers’ request to demonstrate potential layout options</li>
      </ul>
    </div>
    <div class="panel__copy panel__copy--closing">
      <p>The City of Ravensby is geographically located between Las Vegas and Los Angeles where its warm weather, robust labor force, and convenient freeway access offers an ideal setting for indoor cultivation and distribution of medical marijuana.</p>
    </div>
  </section>
</article>

<p class="note">Note: How about a double sided design, where we can add the contact details with some more images behind?</p>

</body>
</html>
```